We need a web design for an existing company that has been in business for 16 years, based in the Dallas-Ft. Worth, Texas area. We also just received a new logo from PixelForge that we want to incorporate with the site. The site should have a professional look and feel that will grow with us. We need the website to include a holding place for project photos that will demonstrate a "before and after" view of our work. We will upload photos of our work once the site is designed. Tarnwick Property Care provides the following services: Pressure Washing, Parking Lot Striping, and Janitorial Services for commercial businesses of all types. We also provide exterior and Interior commercial and residential painting services. We are insured and use bio-friendly cleaners. The site will also need a "Request a Quote" section where people can submit their contact information for a bid from us. This would be just shooting off an email to us once they click submit. We want the site to be professional, clean and simple but with a slick design!
Target Market(s)
Commercial businesses
Industry/Entity Type
Residential
Number of Pages Required
4 page
Look and feel

```html
<!DOCTYPE html>
<html lang="en">
<head>
<meta charset="utf-8">
<title>Tarnwick Property Care</title>
<link rel="stylesheet" href="https://fonts.googleapis.com/css2?family=Oswald:wght@400;600;700&family=Open+Sans:wght@400;600;700&display=swap">
<style>
:root{
  --green:#a6c83a;
  --green-dark:#8eaf2b;
  --ink:#2b2b2b;
  --muted:#777;
  --white:#fff;
}
*{box-sizing:border-box;margin:0;padding:0}
html,body{width:1200px;height:4296px;overflow:hidden}
body{font-family:"Open Sans",Arial,sans-serif;color:var(--ink);background:var(--white);position:relative}
.display{font-family:"Oswald","Arial Narrow",sans-serif;font-weight:700;text-transform:uppercase;letter-spacing:1px}

/* header */
.site-header{position:absolute;top:0;left:0;width:1200px;height:96px;background:var(--white);display:flex;align-items:center;justify-content:space-between;padding:0 70px 0 130px}
.brand{display:flex;align-items:center;gap:12px;font-family:"Open Sans",sans-serif;font-weight:700;font-size:24px;color:var(--green-dark)}
.brand-dot{width:20px;height:20px;border-radius:50%;background:var(--green)}
.main-nav{display:flex;gap:34px;font-size:12px;font-weight:600;color:#555;text-transform:uppercase;align-items:center}
.main-nav .current{border:1px solid #555;padding:8px 14px}

/* hero */
.hero{position:absolute;top:96px;left:0;width:1200px;height:624px;background:linear-gradient(160deg,#3a3f45 0%,#1e2124 45%,#0f1113 100%);text-align:center;color:var(--white)}
.hero-title{position:absolute;top:140px;left:0;width:100%;font-size:92px;line-height:1}
.hero-sub{position:absolute;top:252px;left:0;width:100%;font-family:"Oswald",sans-serif;font-size:32px;line-height:1.2;color:var(--green);text-transform:uppercase;letter-spacing:1px}
.hero-actions{position:absolute;top:318px;left:0;width:100%;display:flex;justify-content:center;gap:40px}
.btn{display:inline-block;font-family:"Oswald",sans-serif;font-size:18px;text-transform:uppercase;letter-spacing:1px;padding:9px 26px;border:2px solid var(--white);color:var(--white)}
.btn-green{border-color:var(--green);color:var(--green)}
.slider-dots{position:absolute;top:408px;left:0;width:100%;display:flex;justify-content:center;align-items:center;gap:18px}
.slider-dots span{width:8px;height:8px;border-radius:50%;background:var(--white)}
.slider-dots .active{width:16px;height:16px;background:none;border:2px solid var(--white)}
.scroll-cue{position:absolute;left:588px;width:24px;height:38px}

/* section titles */
.section-title{position:absolute;left:0;width:100%;text-align:center;font-size:72px;line-height:1.1}
.section-lead{position:absolute;left:0;width:100%;text-align:center;font-size:15px;line-height:1.4;color:var(--muted)}

/* services */
.services{position:absolute;top:720px;left:0;width:1200px;height:770px;background:var(--white)}
.services .section-title{top:55px;color:var(--green)}
.services .section-lead{top:152px}
.service{position:absolute;top:240px;width:260px;text-align:center}
.service-badge{width:190px;height:190px;margin:0 auto;border-radius:50%;background:var(--green);color:var(--white);display:flex;flex-direction:column;justify-content:center}
.service-badge strong{font-family:"Oswald",sans-serif;font-size:38px;font-weight:600;text-transform:uppercase;line-height:1.1}
.service-badge small{font-size:17px;font-weight:600;color:#2b3a08}
.service p{margin-top:38px;font-size:14px;line-height:1.55;color:var(--muted)}
.service .btn-small{display:inline-block;margin-top:22px;font-size:13px;text-transform:uppercase;color:var(--muted);border:1px solid #bbb;padding:5px 18px}

/* work */
.work{position:absolute;top:1490px;left:0;width:1200px;height:766px;background:linear-gradient(150deg,#2f3439 0%,#15171a 55%,#24282c 100%);color:var(--white)}
.work .section-title{top:50px}
.work .section-lead{top:140px;color:#ccc}
.gallery-thumb{position:absolute;left:160px;width:200px;height:104px;background:linear-gradient(135deg,#c99a4a,#5d6f88)}
.gallery-main{position:absolute;top:190px;left:385px;width:660px;height:310px;background:linear-gradient(120deg,#e8d7b8 0%,#d5a530 40%,#7d8894 100%)}
.gallery-caption{position:absolute;top:500px;left:385px;width:660px;height:145px;background:#0c0d0e;padding:20px 28px}
.gallery-caption h3{font-size:20px;font-weight:700;text-transform:uppercase;margin-bottom:10px}
.gallery-caption p{font-size:14px;line-height:1.6;color:#cfcfcf}

/* testimonials */
.testimonials{position:absolute;top:2256px;left:0;width:1200px;height:1054px;background:var(--white)}
.testimonials .section-title{top:45px;color:var(--green)}
.testimonials .section-lead{top:138px}
.avatar{position:absolute;width:170px;height:170px;border-radius:50%;background:linear-gradient(160deg,#c9c3bb,#6b645c)}
.quote-card{position:absolute;width:705px;height:155px;background:var(--green);padding:20px 30px}
.quote-card h4{font-size:22px;font-weight:700;text-transform:uppercase;margin-bottom:8px;color:#1e2a05}
.quote-card p{font-size:14px;line-height:1.6;color:#2d3b0a}
.quote-card svg{position:absolute;top:60px}

/* request quote */
.request{position:absolute;top:3310px;left:0;width:1200px;height:866px;background:linear-gradient(160deg,#2b2f33 0%,#15171a 50%,#2e3236 100%);color:var(--white)}
.request .section-title{top:55px}
.request .section-lead{top:148px;color:#ccc}
.quote-form{position:absolute;top:240px;left:300px;width:610px}
.field{display:block;width:610px;height:56px;border:1px solid #666;background:rgba(0,0,0,.35);color:#bbb;font-size:15px;padding:16px 18px;margin-bottom:19px}
.field-message{height:225px}
.btn-send{display:inline-block;margin-top:8px;background:var(--green);color:var(--white);font-family:"Oswald",sans-serif;font-size:18px;text-transform:uppercase;padding:10px 24px}

/* footer */
.site-footer{position:absolute;top:4176px;left:0;width:1200px;height:120px;background:var(--green);display:flex;align-items:center;justify-content:space-between;padding:0 130px;color:var(--white);font-size:14px}
.social{display:flex;gap:16px}
.social span{width:46px;height:46px;border-radius:50%;border:2px solid var(--white)}
</style>
</head>
<body>

<header class="site-header">
  <div class="brand"><span class="brand-dot"></span>Tarnwick Property Care</div>
  <nav class="main-nav">
    <span class="current">Home</span><span>Residential Service</span><span>Painting</span><span>Pictures</span><span>Main</span><span>About</span><span>Contact</span>
  </nav>
</header>

<section class="hero" role="img" aria-label="Dark photo of a glass office building looking upward">
  <h1 class="hero-title display">Welcome to Tarnwick</h1>
  <p class="hero-sub">Property Care</p>
  <div class="hero-actions"><span class="btn btn-green">Read More</span><span class="btn">Get Started</span></div>
  <div class="slider-dots"><span></span><span class="active"></span><span></span></div>
  <svg class="scroll-cue" style="top:480px" viewBox="0 0 24 38"><rect x="2" y="2" width="20" height="34" rx="10" fill="none" stroke="#fff" stroke-width="2"/><line x1="12" y1="9" x2="12" y2="15" stroke="#fff" stroke-width="2"/></svg>
</section>

<section class="services">
  <h2 class="section-title display">Services</h2>
  <p class="section-lead">Tarnwick Property Care provides professional pressure washing and painting for all property types.</p>
  <div class="service" style="left:165px">
    <div class="service-badge"><strong>Building</strong><small>Clean</small></div>
    <p>Commercial cleaning done right. Eco-friendly products, insured crews and reliable scheduling for every site.</p>
    <span class="btn-small">Read More</span>
  </div>
  <div class="service" style="left:470px">
    <div class="service-badge"><strong>Building</strong><small>Maintenance</small></div>
    <p>Pressure washing and janitorial care. Bio-friendly cleaners, trained staff and steady service for every building.</p>
    <span class="btn-small">Read More</span>
  </div>
  <div class="service" style="left:775px">
    <div class="service-badge"><strong>Building</strong><small>Parking</small></div>
    <p>Parking lot striping made simple. Crisp lines, durable paint and quick turnaround for every lot size.</p>
    <span class="btn-small">Read More</span>
  </div>
  <svg class="scroll-cue" style="top:690px" viewBox="0 0 24 38"><rect x="2" y="2" width="20" height="34" rx="10" fill="none" stroke="#a6c83a" stroke-width="2"/><line x1="12" y1="9" x2="12" y2="15" stroke="#a6c83a" stroke-width="2"/></svg>
</section>

<section class="work" aria-label="Our work">
  <h2 class="section-title display">Our Work</h2>
  <p class="section-lead">We have an eye for perfection.</p>
  <div class="gallery-thumb" style="top:190px" role="img" aria-label="Project photo: painter on a ladder"></div>
  <div class="gallery-thumb" style="top:300px" role="img" aria-label="Project photo: crew working on a facade"></div>
  <div class="gallery-thumb" style="top:410px;height:90px" role="img" aria-label="Project photo: worker cleaning windows"></div>
  <div class="gallery-main" role="img" aria-label="Featured project photo: worker in a yellow hard hat"></div>
  <div class="gallery-caption">
    <h3>Lorem Ipsum</h3>
    <p>Before and after views of our recent projects. Pressure washing, parking lot striping, janitorial service and interior and exterior painting for commercial and residential clients across the region.</p>
  </div>
  <svg class="scroll-cue" style="top:690px" viewBox="0 0 24 38"><rect x="2" y="2" width="20" height="34" rx="10" fill="none" stroke="#fff" stroke-width="2"/><line x1="12" y1="9" x2="12" y2="15" stroke="#fff" stroke-width="2"/></svg>
</section>

<section class="testimonials">
  <h2 class="section-title display">Testimonials</h2>
  <p class="section-lead">We also provide exterior and interior commercial and residential painting services.</p>

  <div class="avatar" style="top:255px;left:120px" role="img" aria-label="Client portrait"></div>
  <div class="quote-card" style="top:240px;left:325px">
    <svg style="left:-20px" width="20" height="30" viewBox="0 0 20 30"><polygon points="20,0 20,30 0,15" fill="#a6c83a"/></svg>
    <h4>Lorem Ipsum</h4>
    <p>Tarnwick kept our storefront spotless and striped the whole parking lot over one weekend. The crew was on time, careful and friendly, and the price matched the quote exactly.</p>
  </div>

  <div class="avatar" style="top:475px;left:905px" role="img" aria-label="Client portrait"></div>
  <div class="quote-card" style="top:470px;left:200px">
    <svg style="right:-20px" width="20" height="30" viewBox="0 0 20 30"><polygon points="0,0 0,30 20,15" fill="#a6c83a"/></svg>
    <h4>Lorem Ipsum</h4>
    <p>Our office building looks brand new after their pressure washing and fresh exterior paint. They used safe cleaners around our landscaping and left every area neat and clean.</p>
  </div>

  <div class="avatar" style="top:715px;left:120px" role="img" aria-label="Client portrait"></div>
  <div class="quote-card" style="top:720px;left:325px">
    <svg style="left:-20px" width="20" height="30" viewBox="0 0 20 30"><polygon points="20,0 20,30 0,15" fill="#a6c83a"/></svg>
    <h4>Lorem Ipsum</h4>
    <p>We have used their janitorial team for years and never had a missed night. Communication is easy, the staff is trustworthy, and our tenants always notice the difference in quality.</p>
  </div>

  <svg class="scroll-cue" style="top:950px" viewBox="0 0 24 38"><rect x="2" y="2" width="20" height="34" rx="10" fill="none" stroke="#a6c83a" stroke-width="2"/><line x1="12" y1="9" x2="12" y2="15" stroke="#a6c83a" stroke-width="2"/></svg>
</section>

<section class="request" role="img" aria-label="Dark photo of hands typing on a laptop">
  <h2 class="section-title display">Request a Quote</h2>
  <p class="section-lead">Send us a note, and we will call you right back.</p>
  <form class="quote-form">
    <span class="field">Your Name</span>
    <span class="field">Your Email</span>
    <span class="field">Subject</span>
    <span class="field field-message">Your Message</span>
    <span class="btn-send">Send</span>
  </form>
</section>

<footer class="site-footer">
  <span>Copyright &copy; 2015</span>
  <div class="social"><span></span><span></span><span></span></div>
</footer>

</body>
</html>
```